Flyer-Design für Dienst für professionelle Fahrzeugpflege
Zielgruppe
Dienst für professionelle Fahrzeugpflege, Nano- Keramikversiegelung, 3-Stufen Politur, Hol- und Bringdienst Autowäsche, Politur, Innenraumreinigung, Geruchsentfernung, Flecken entfernen auf den Sitzen / Polster
Autoliebhaber, junge Leute, Geschäftsführer, Firmen, Leute die Ihr auto nicht mehr alleine Waschen können/möchten
Aufgabenstellung
Das Design sollte sehr Edel aber zugleich sportlich aussehen. Es sollte die junge Zielgruppe sowie den erfolgreichen Geschäftsführer ansprechen.

```html
<!DOCTYPE html>
<html lang="de">
<head>
<meta charset="utf-8">
<title>Unsere Leistungen im Überblick</title>
<link rel="stylesheet" href="https://fonts.googleapis.com/css2?family=Kreon:wght@700&family=Kurale&display=swap">
<style>
  :root {
    --bg-dark: #2f2f2f;
    --bg-mid: #3d3d3d;
    --bg-light: #4a4a4a;
    --divider: #232323;
    --text: #ffffff;
    --photo-wash-a: #2b2b2b;
    --photo-wash-b: #8a8a8a;
    --photo-polish-a: #1e1e1e;
    --photo-polish-b: #bdbdbd;
  }
  * { margin: 0; padding: 0; box-sizing: border-box; }
  html, body { width: 1134px; height: 1200px; overflow: hidden; }
  body {
    position: relative;
    background: linear-gradient(160deg, var(--bg-mid) 0%, var(--bg-dark) 35%, var(--bg-light) 55%, var(--bg-dark) 75%, var(--bg-mid) 100%);
    color: var(--text);
    font-family: "Kurale", Georgia, serif;
  }
  .sheen {
    position: absolute; inset: 0;
    background: radial-gradient(ellipse 60% 18% at 45% 48%, rgba(255,255,255,0.10), transparent 70%),
                radial-gradient(ellipse 40% 14% at 80% 20%, rgba(255,255,255,0.07), transparent 70%);
  }
  .divider {
    position: absolute; left: 565px; top: 0; width: 6px; height: 1200px;
    background: var(--divider);
  }
  .panel { position: absolute; top: 0; height: 1200px; }
  .panel-left { left: 0; width: 565px; }
  .panel-right { left: 571px; width: 563px; }
  .block { position: absolute; left: 0; right: 0; text-align: center; }
  .heading {
    font-family: "Kreon", Georgia, serif; font-weight: 700;
    text-decoration: underline; text-underline-offset: 5px; text-decoration-thickness: 2px;
  }
  .page-title { font-size: 40px; line-height: 71px; }
  .service-title { font-size: 30px; line-height: 40px; }
  .service-title.large { font-size: 32px; line-height: 53px; }
  .copy { font-size: 22px; line-height: 44px; }
  .copy.underlined { text-decoration: underline; text-underline-offset: 4px; }
  .copy.strong {
    font-family: "Kreon", Georgia, serif; font-weight: 700; font-size: 24px; line-height: 43.5px;
    text-decoration: underline; text-underline-offset: 4px;
  }
  .photo { position: absolute; }
  .photo-wash {
    left: 72px; top: 563px; width: 424px; height: 267px;
    background: linear-gradient(120deg, var(--photo-wash-a) 0%, var(--photo-wash-b) 55%, var(--photo-wash-a) 100%);
  }
  .photo-polish {
    left: 73px; top: 69px; width: 423px; height: 283px;
    background: linear-gradient(150deg, var(--photo-polish-a) 0%, var(--photo-polish-b) 50%, var(--photo-polish-a) 100%);
  }
</style>
</head>
<body>
  <div class="sheen"></div>
  <div class="divider"></div>

  <section class="panel panel-left">
    <h1 class="block heading page-title" style="top:61px;">Unsere Leistungen im<br>Überblick</h1>

    <h2 class="block heading service-title" style="top:272px;">Abhol- und Bringservice</h2>
    <p class="block copy" style="top:321px;">Egal ob Sie zuhause oder an ihrem<br>Arbeitsplatz sind. Wir kommen ihr<br>Fahrzeug abholen und bringen es<br>nach der Reinigung wieder sicher<br>zurück.</p>

    <div class="photo photo-wash" role="img" aria-label="Foto: Handwäsche eines schwarzen Autos mit Schaum und Schwamm"></div>

    <h2 class="block heading service-title" style="top:880px;">Autowäsche</h2>
    <p class="block copy underlined" style="top:928px;">Hier könnten Infos stehn die Ihre<br>Autowäsche für den Kunden<br>interessanter machen können z.b.<br>Besonders schonendeHandwäsche o.ä.</p>
  </section>

  <section class="panel panel-right">
    <div class="photo photo-polish" role="img" aria-label="Foto: Lackpolitur an einem nassen schwarzen Auto mit Handschuh"></div>

    <h2 class="block heading service-title" style="top:398px;">Lackpflege</h2>
    <p class="block copy" style="top:447px;">Wir polieren ihren Lack mit einer<br>3 Stufen Politur</p>

    <p class="block copy underlined" style="top:578px;">Kuzre Info über die 3 Stufen</p>
    <ol class="block copy" style="top:622px; list-style:none;">
      <li>1. erste Stufe</li>
      <li>2. zweite Stufe</li>
      <li>3. dritte Stufe</li>
    </ol>

    <h2 class="block heading service-title large" style="top:825px;">Nano<br>Keramikversiegelung</h2>
    <p class="block copy strong" style="top:933px;">Hier vielleicht eine kurze<br>Erklärung was es mit der<br>Nanoversiegelung aufsich hat</p>
  </section>
</body>
</html>
```